Corvath Holdings, LLC

We are a design build general contracting company.
We work with commercial accounts and private developers. We build retail spaces, restaurants and housing projects.
Im looking for a clean professional type of logo incorporating a roman flavor, think ionic columns and pedestals.
Two toned colorway.
I like unusual fonts and Im not afraid to do something bold with the logo.
Contact Information for Business Card
Marisol Brenkowitz
318-472-9051 corvathmb@mailvexo.com
Font styles to use
Decorative
Colors
Designer to choose colors to be used in the design.
Requirements
Should not have
- I don't like reds pinks.

```html
<!DOCTYPE html>
<html lang="en">
<head>
<meta charset="utf-8">
<title>Corvath Holdings, LLC — Business Card</title>
<link rel="stylesheet" href="https://fonts.googleapis.com/css2?family=Courier+Prime:wght@400;700&display=swap">
<style>
  :root {
    --backdrop: #2a2b30;
    --paper-light: #f1ebda;
    --paper-mid: #e6dcc4;
    --paper-dark: #d8ccb0;
    --ink: #1d1a17;
    --column-tone: #7a7168;
    --column-light: #b9b0a4;
  }
  * { margin: 0; padding: 0; box-sizing: border-box; }
  html, body {
    width: 1200px; height: 864px; overflow: hidden;
    background: var(--backdrop);
  }
  .canvas {
    position: relative; width: 1200px; height: 864px;
  }
  .card {
    position: absolute; left: 280px; width: 640px; height: 366px;
    border-radius: 22px; overflow: hidden;
    background: radial-gradient(ellipse at 45% 40%, var(--paper-light) 0%, var(--paper-mid) 60%, var(--paper-dark) 100%);
    color: var(--ink);
    font-family: "Courier Prime", "Courier New", monospace;
  }
  .card--front { top: 48px; }
  .card--back { top: 450px; }

  .column-art {
    position: absolute;
    background: linear-gradient(180deg, var(--column-tone) 0%, var(--column-light) 55%, var(--column-tone) 100%);
    opacity: 0.85;
  }
  .card--front .column-art {
    right: 0; top: 0; width: 180px; height: 210px;
    border-bottom-left-radius: 90px 40px;
  }
  .card--back .column-art {
    left: 0; bottom: 0; width: 240px; height: 260px;
    border-top-right-radius: 110px 60px;
  }

  .brand {
    position: absolute; text-align: center;
  }
  .card--front .brand { left: 50px; top: 120px; width: 370px; }
  .card--back .brand { left: 270px; top: 70px; width: 340px; }

  .brand__mark {
    display: block; width: 28px; height: 28px;
    margin: 0 auto 14px; background: var(--ink);
  }
  .brand__name {
    font-weight: 700; font-size: 24px; letter-spacing: 0.4px;
    text-transform: uppercase; line-height: 1.1; white-space: nowrap;
  }
  .brand__tagline {
    font-weight: 400; font-size: 13.5px; letter-spacing: 1.2px;
    text-transform: uppercase; margin-top: 5px; white-space: nowrap;
  }

  .contact {
    position: absolute; left: 270px; top: 200px; width: 340px;
    text-align: center;
  }
  .contact__name { font-size: 21px; margin-bottom: 14px; }
  .contact__line { font-size: 14px; line-height: 1.55; }
</style>
</head>
<body>
<main class="canvas">
  <section class="card card--front" aria-label="Card front">
    <div class="column-art" role="img" aria-label="Engraved ionic column capital with volute"></div>
    <div class="brand">
      <span class="brand__mark" aria-hidden="true"></span>
      <div class="brand__name">Corvath Holdings, LLC</div>
      <div class="brand__tagline">Construction &amp; Development</div>
    </div>
  </section>

  <section class="card card--back" aria-label="Card back">
    <div class="column-art" role="img" aria-label="Engraved ionic column with volute and fluted shaft"></div>
    <div class="brand">
      <span class="brand__mark" aria-hidden="true"></span>
      <div class="brand__name">Corvath Holdings, LLC</div>
      <div class="brand__tagline">Construction &amp; Development</div>
    </div>
    <div class="contact">
      <div class="contact__name">Marisol Brenkowitz</div>
      <div class="contact__line">318-472-9051</div>
      <div class="contact__line">corvathmb@mailvexo.com</div>
    </div>
  </section>
</main>
</body>
</html>
```